Need Business Card for our Indian Grocery Store

Industry/Entity Type

Grocery Store

Contact Information for Business Card

Manoj Baweja
Director

Store Locations:

Brackenvale
482 Elm Parade
P: 03 9172 5843

Millbrook Rise
613 Carlow Road
P: 03 9238 6014

email: kvtmarts@mailnest.example

Requirements
Must have
• Our logo Colours

```html
<!DOCTYPE html>
<html lang="en">
<head>
<meta charset="utf-8">
<title>KVT Grocers – Business Card</title>
<link rel="stylesheet" href="https://fonts.googleapis.com/css2?family=Roboto:wght@400;500;700&display=swap">
<style>
  :root {
    --brand-red: #e31e2b;
    --brand-red-soft: #ea4a3f;
    --card-white: #ffffff;
    --ink: #1d1d1d;
    --rule: #3a3a3a;
    --stage: #2b2b2b;
  }
  * { box-sizing: border-box; margin: 0; padding: 0; }
  html, body { width: 1200px; height: 900px; overflow: hidden; }
  body {
    background: var(--stage);
    font-family: "Roboto", Arial, sans-serif;
    display: flex;
    flex-direction: column;
    align-items: center;
    justify-content: center;
    gap: 36px;
  }
  .card {
    width: 700px;
    height: 400px;
    border-radius: 26px;
    overflow: hidden;
    position: relative;
  }

  /* Back side */
  .card--back { background: var(--brand-red); }
  .back-pattern {
    position: absolute; inset: 0;
    background: linear-gradient(135deg, var(--brand-red) 0%, var(--brand-red-soft) 100%);
  }
  .back-mark {
    position: absolute;
    right: 40px; bottom: 160px;
    color: var(--card-white);
    font-weight: 700;
    font-size: 34px;
    line-height: 1;
    letter-spacing: 1px;
    white-space: nowrap;
  }

  /* Front side */
  .card--front {
    background: var(--card-white);
    display: flex;
    align-items: center;
  }
  .brand {
    width: 380px;
    flex: none;
    text-align: center;
    color: var(--brand-red);
    font-weight: 700;
    font-size: 58px;
    line-height: 1;
    letter-spacing: 1px;
    white-space: nowrap;
    padding-top: 40px;
  }
  .divider {
    width: 1.5px;
    height: 250px;
    flex: none;
    background: var(--rule);
    margin-top: 20px;
  }
  .contact {
    padding-left: 30px;
    padding-right: 20px;
    color: var(--ink);
    font-size: 16px;
    line-height: 1.3;
    padding-top: 10px;
    white-space: nowrap;
  }
  .contact__name { font-size: 25px; font-weight: 500; }
  .contact__role { color: var(--brand-red); font-size: 19px; margin-bottom: 6px; }
  .contact__row { display: flex; align-items: center; gap: 9px; }
  .store { margin-top: 14px; }
  .icon { width: 20px; height: 20px; flex: none; }
</style>
</head>
<body>

  <section class="card card--back" aria-label="Card back">
    <div class="back-pattern" role="img" aria-label="Faint repeating brand pattern on red"></div>
    <div class="back-mark">KVT Grocers</div>
  </section>

  <section class="card card--front" aria-label="Card front">
    <div class="brand">KVT Grocers</div>

    <div class="divider"></div>

    <div class="contact">
      <div class="contact__name">Manoj Baweja</div>
      <div class="contact__role">Director</div>
      <div class="contact__row">
        <svg class="icon" viewBox="0 0 20 20" aria-hidden="true">
          <rect width="20" height="20" rx="3" fill="var(--brand-red)"/>
          <rect x="4" y="6" width="12" height="8" fill="none" stroke="#fff" stroke-width="1.5"/>
          <path d="M4 6 L10 11 L16 6" fill="none" stroke="#fff" stroke-width="1.5"/>
        </svg>
        <span>kvtmarts@mailnest.example</span>
      </div>

      <div class="store">
        <div>Brackenvale</div>
        <div>482 Elm Parade</div>
        <div class="contact__row">
          <svg class="icon" viewBox="0 0 20 20" aria-hidden="true">
            <rect width="20" height="20" rx="3" fill="var(--brand-red)"/>
            <path d="M6 4.5 L8.3 4.5 L9 7.6 L7.6 8.8 Q8.7 11.3 11.2 12.4 L12.4 11 L15.5 11.7 L15.5 14 Q15.5 15.5 14 15.5 Q4.5 15 4.5 6 Q4.5 4.5 6 4.5 Z" fill="#fff"/>
          </svg>
          <span>03 9172 5843</span>
        </div>
      </div>

      <div class="store">
        <div>Millbrook Rise</div>
        <div>613 Carlow Road</div>
        <div class="contact__row">
          <svg class="icon" viewBox="0 0 20 20" aria-hidden="true">
            <rect width="20" height="20" rx="3" fill="var(--brand-red)"/>
            <path d="M6 4.5 L8.3 4.5 L9 7.6 L7.6 8.8 Q8.7 11.3 11.2 12.4 L12.4 11 L15.5 11.7 L15.5 14 Q15.5 15.5 14 15.5 Q4.5 15 4.5 6 Q4.5 4.5 6 4.5 Z" fill="#fff"/>
          </svg>
          <span>03 9238 6014</span>
        </div>
      </div>
    </div>
  </section>

</body>
</html>
```